Commercial Web Site for software product

Ledgerly is a GDPR compliant Membership, Contact Management & List Management solution. It is an ideal replacement for any organisation or company still using spreadsheets, email clients, simple database or paper-based system to manage contact data, mail lists, and other personal information.
The target market will be Clubs/Associations in the EU.
The design will need to be a fluid design and suitable for mobile devices. The home page will contain most of the web site content, enabling a user to scroll through all the relevant information on one page. There will be a single sub page design required for supporting information.
The web site will need to support two language versions - English and German (Language selection option required). However, the build requirements will be for a static HTML site (no database) in English only. We will duplicate and make the German version ourselves.
The attached document is the first draft of the home page content. Whilst it is a little wordy, it should convey the main information that we wish to get across.
Please note: We would prefer not to use photographs for the main imagery, we feel vector graphics would be a better option . As a guide, the following design: https://en.pixelvane.example/profiles/Marlowe/designs/5502147 may provide an insight into how we imagine the home page working and contains all the key elements we would expect to be covered.
The logo contained in the attached document can be split into a logo and text. Feel free to use only the logo (without text) or separate and place the text alongside etc., We do not want to change the logo, however, how you chose to use it is up to you.
Colour's are also optional. We like the blue, but are open to alternative ideas.
The testimonials section, should contain all the questions (3) and several of the associated answers shown. Questions/Answers may be separated into speech bubbles or similar. Not all answers will be used, but are there to provide some content.
The sub pages will be used to provide background on the GDPR requirements, our Service Offering, About Us (possibly), and a contact page.
Updates
The design budget is now guaranteed.
Whilst we have no intention not to move forward with this project, I understand the 'lack of commitment' from our side may be a negative.
Once we have reviewed all submissions - we will decide upon our preferred submission.
We will only request changes from one or two designers, and will make it clear how many other designers are in the running. This I believe is fair, as you probably need this information before deciding whether to submit any changes requested!
My hope is we have a home page that enables a visitor to clearly understand what we are offering, without having to drill down into various sub pages or sections to understand the basics. I appreciate we need to write appropriate content, but the design itself should feel uncluttered and fluid.
Hopefully some of you really talented designers can throw some ideas into the pot. The concept is more important than the detail.
Thanks for considering this project.
Coding
Number of Pages Required
Font styles to use
Colors
Look and feel

```html
<!DOCTYPE html>
<html lang="en">
<head>
<meta charset="utf-8">
<title>Ledgerly – GDPR Compliant Membership and Contact Management</title>
<link rel="stylesheet" href="https://fonts.googleapis.com/css2?family=Barlow:wght@300;400&family=Inter:wght@400;500;600;700&family=Plus+Jakarta+Sans:wght@800&display=swap">
<style>
:root{
  --backdrop:#5f5f5f;
  --ink-dark:#11141e;
  --panel-dark:#1d2130;
  --light:#f8f8f8;
  --white:#ffffff;
  --blue:#2f8ff0;
  --blue-deep:#0b57d0;
  --text-dark:#1b1d26;
  --muted:#7c8090;
  --muted-light:#a6abb8;
  --line:#e4e5ea;
  --lime:#a6d84a;
  --orange:#f26a2e;
  --stone:#d8d6d0;
  --graphite:#3a3c45;
}
*{box-sizing:border-box;margin:0;padding:0}
html,body{width:1200px;height:1200px;overflow:hidden;background:var(--backdrop)}
body{font-family:"Inter",sans-serif}
.stage{position:absolute;left:0;top:0;width:1932px;height:1932px;transform:scale(.62112);transform-origin:0 0}
.page{position:absolute;left:741px;top:40px;width:391px;height:1867px;background:var(--ink-dark);overflow:hidden}
.abs{position:absolute}
.section-dark{position:absolute;left:0;width:391px;background:var(--ink-dark);color:var(--white)}
.section-light{position:absolute;left:0;width:391px;background:var(--light);color:var(--text-dark)}
.heading{font-family:"Barlow",sans-serif;font-weight:300;font-size:11.5px;line-height:15px}
.center{text-align:center;left:0;width:391px}
.small{font-size:3.6px;line-height:7px;color:var(--muted)}
.btn{position:absolute;font-size:3.6px;font-weight:600;display:flex;align-items:center;justify-content:center;background:var(--blue);color:var(--white)}
.placeholder{position:absolute}
.brand{display:flex;align-items:center;gap:3px;font-size:5px;font-weight:700;color:var(--white)}
.brand i{width:5px;height:5px;background:var(--blue);display:block}
.nav a{position:absolute;top:9px;font-size:4px;color:var(--white);text-decoration:none}
.hero-title{font-family:"Plus Jakarta Sans",sans-serif;font-weight:800;font-size:14px;line-height:17px;color:var(--white)}
.feature{position:absolute;top:313px;width:102px;height:66px;background:var(--white);border-bottom:2px solid var(--text-dark);padding:8px 7px}
.feature.active{border-bottom-color:var(--blue)}
.feature svg{display:block}
.feature h3{font-size:4px;font-weight:500;margin:6px 0 5px}
.feature p{font-size:3.6px;line-height:6.5px;color:var(--muted)}
.dash{position:absolute;left:38px;top:502px;width:316px;height:194px;background:var(--white);border-radius:2px;overflow:hidden}
.dash-side{position:absolute;left:0;top:0;width:55px;height:194px;background:var(--panel-dark);padding:7px 5px;color:var(--white)}
.dash-side .row{display:flex;align-items:center;gap:3px;font-size:3px;color:#c8ccd6;margin-top:6px}
.dash-side .row i{width:3px;height:3px;background:#8a90a0;border-radius:1px;display:block}
.dash-main{position:absolute;left:55px;top:0;right:0;bottom:0;background:#eef0f4}
.tabs span{position:absolute;top:963px;font-size:4px}
.plan{position:absolute;top:1216px;background:var(--white);height:164px;text-align:center;padding-top:14px}
.plan h4{font-size:3.6px;font-weight:700;letter-spacing:.2px}
.plan .tag{font-size:3px;color:var(--muted);margin-top:2px}
.plan .price{font-size:11px;font-weight:700;margin-top:9px}
.plan .price sup,.plan .price sub{font-size:3.4px;font-weight:400;color:var(--muted)}
.plan ul{list-style:none;text-align:left;padding-left:9px;margin-top:8px}
.plan li{font-size:3.4px;line-height:8.8px;display:flex;align-items:center;gap:3px}
.plan li::before{content:"";width:3px;height:3px;border:0.7px solid var(--muted);border-radius:50%}
.plan li.off{color:#c1c3ca}
.plan .cta{position:absolute;left:9px;right:9px;bottom:22px;height:11px;background:#ececef;font-size:3.4px;font-weight:600;display:flex;align-items:center;justify-content:center}
.plan .cta.primary{background:var(--blue);color:var(--white)}
.plan .note{position:absolute;left:0;right:0;bottom:10px;font-size:3px;color:#b0b3bb}
.quote{position:absolute;font-size:3.6px;line-height:6.5px;color:#dfe2ea}
.who{position:absolute;font-size:3.4px;font-weight:600;color:var(--white)}
.role{position:absolute;font-size:3px;color:var(--muted-light)}
.footer h5{position:absolute;top:1798px;font-size:3.6px;font-weight:600;color:var(--white)}
.footer a{position:absolute;font-size:3px;color:var(--muted-light);text-decoration:none}
</style>
</head>
<body>
<div class="stage">
<main class="page">

  <section class="section-dark" style="top:0;height:216px">
    <div class="brand abs" style="left:38px;top:8px"><i></i>Ledgerly</div>
    <nav class="nav">
      <a style="left:72px">Demos</a><a style="left:97px">About</a><a style="left:120px">Blog</a><a style="left:141px">Pages</a><a style="left:165px">Contact</a>
    </nav>
    <div class="btn" style="left:318px;top:5px;width:32px;height:12px;background:var(--blue-deep)">Get Started</div>
    <h1 class="hero-title abs" style="left:38px;top:58px">The All-in-One GDPR<br>Compliant Membership<br>and Contact Management<br>Tool</h1>
    <p class="small abs" style="left:38px;top:127px;width:158px;color:var(--muted-light)">Discover Ledgerly – Your Comprehensive Solution for Managing Membership, Contacts, and Personalized Information while Ensuring GDPR Compliance.</p>
    <div class="btn" style="left:38px;top:162px;width:49px;height:15px">Get Started</div>
    <div class="btn" style="left:91px;top:162px;width:49px;height:15px;background:var(--white);color:var(--text-dark)">View Packages</div>
    <div class="placeholder" role="img" aria-label="Isometric blocks illustration in lime, graphite, orange and stone" style="left:237px;top:47px;width:116px;height:131px;background:linear-gradient(135deg,var(--lime) 0%,var(--graphite) 40%,var(--orange) 70%,var(--stone) 100%);opacity:.85"></div>
  </section>

  <section class="section-light" style="top:216px;height:193px">
    <h2 class="heading abs center" style="top:30px">These features make your hosting<br>work faster</h2>
    <p class="small abs center" style="top:66px">Make your visitors happy and reduce website loading time.<br>Take full advantage of speed and power.</p>
  </section>
  <article class="feature" style="left:38px">
    <svg width="8" height="8" viewBox="0 0 8 8"><circle cx="4" cy="4" r="3.2" fill="none" stroke="#1b1d26" stroke-width=".7"/><circle cx="4" cy="4.6" r="1.4" fill="#e04848"/></svg>
    <h3>Remote Daily Backup</h3>
    <p>Your website data is always secure &amp; protected with automatic daily backups and easily restore data with 1 click.</p>
  </article>
  <article class="feature active" style="left:145px">
    <svg width="8" height="8" viewBox="0 0 8 8"><path d="M4 .8 7 2v2.2C7 6 5.6 7 4 7.4 2.4 7 1 6 1 4.2V2Z" fill="none" stroke="#1b1d26" stroke-width=".7"/><circle cx="4.4" cy="4.4" r="1.3" fill="#2f8ff0"/></svg>
    <h3>Worldwide Cybersecurity</h3>
    <p>Ultimate cybersecurity it blocks 99.99% of web attacks and monitors your real website 24/7, real-time worldwide.</p>
  </article>
  <article class="feature" style="left:252px">
    <svg width="8" height="8" viewBox="0 0 8 8"><circle cx="4" cy="4" r="3.2" fill="none" stroke="#1b1d26" stroke-width=".7"/><circle cx="4.4" cy="4.8" r="1.4" fill="#f2b630"/></svg>
    <h3>Scale to Success</h3>
    <p>We are committed to deliver practical performance, ironclad security and seamless scalability for your websites.</p>
  </article>

  <section class="section-dark" style="top:409px;height:697px"></section>
  <h2 class="heading abs" style="left:38px;top:440px;color:var(--white)">Your websites deserve fast,<br>secure and also reliable hosting</h2>
  <p class="small abs" style="left:225px;top:446px;width:126px;color:var(--muted-light)">Focus on your business and avoid all the web hosting hassles. Our managed hosting guarantees unmatched performance, reliability and choice with 24/7 support that acts as your extended team, making Skyforge.</p>

  <div class="dash">
    <div class="dash-side">
      <div style="font-size:4px;font-weight:700">Ledgerly</div>
      <div class="row" style="margin-top:14px;color:#fff"><i></i>Dashboard</div>
      <div class="row"><i></i>Posts</div>
      <div class="row"><i></i>Categories</div>
      <div class="row"><i></i>Media</div>
      <div class="row"><i></i>Pages</div>
      <div class="row"><i></i>Comments</div>
      <div class="row" style="font-size:2.6px;color:#6f7585">PLUGINS</div>
      <div class="row"><i></i>Appearance</div>
      <div class="row"><i></i>Extensions</div>
      <div class="row"><i></i>Users</div>
      <div class="row"><i></i>Settings</div>
      <div class="abs" style="left:4px;bottom:8px;width:46px;height:12px;background:#2b3042;border-radius:2px;font-size:2.6px;padding:3px 0 0 12px;color:#c8ccd6">Elias Brandt</div>
    </div>
    <div class="dash-main">
      <div class="abs" style="left:5px;top:4px;width:60px;height:8px;background:var(--white);border-radius:4px;font-size:2.6px;color:var(--muted);padding:2px 0 0 7px">Enter keywords…</div>
      <div class="abs" style="left:4px;top:20px;font-size:4.2px;font-weight:700;color:var(--text-dark)">Innovative platform</div>
      <div class="abs" style="left:4px;top:34px;right:4px;bottom:10px;background:var(--white)">
        <div class="abs" style="left:5px;top:4px;font-size:2.6px;color:var(--muted)">• On time &nbsp; • Manage files &nbsp; • Scale to Success</div>
        <div class="placeholder" role="img" aria-label="Isometric cloud server illustration in blue" style="left:80px;top:20px;width:110px;height:90px;background:radial-gradient(circle,#8cc4f7 0%,#d9ebfb 60%,#ffffff 100%)"></div>
        <div class="abs" style="left:0;right:0;top:125px;text-align:center;font-size:3.6px;font-weight:600;color:var(--text-dark)">Cloud Hosting for PressKit</div>
        <div class="btn" style="left:113px;top:133px;width:36px;height:8px;font-size:2.8px">Register Now</div>
      </div>
    </div>
  </div>

  <div class="placeholder" role="img" aria-label="Isometric blocks illustration in orange, lime, stone and graphite" style="left:38px;top:725px;width:110px;height:140px;background:linear-gradient(160deg,var(--graphite) 0%,var(--stone) 40%,var(--lime) 60%,var(--orange) 100%);opacity:.85"></div>
  <h2 class="heading abs" style="left:199px;top:748px;color:var(--white)">The Ultimate GDPR Compliant<br>Solution for Membership and<br>Contact Management</h2>
  <p class="small abs" style="left:199px;top:796px;width:156px;color:var(--muted-light)">Boost Efficiency, Ensure Data Compliance, and Simplify Operations with Ledgerly – The Perfect Solution for Organizations Still Relying on spreadsheets, email clients, or Paper-based Systems.</p>
  <div class="btn" style="left:199px;top:831px;width:48px;height:13px">Explore Now</div>

  <h2 class="heading abs center" style="top:896px;color:var(--white)">Innovative hosting platform built team<br>empowerment</h2>
  <p class="small abs center" style="top:929px;color:var(--muted-light)">Our migration specialists will migrate as many websites as you ask, free of charge.<br>There will be no downtime, and we'll also ensure that they work properly.</p>
  <div class="tabs">
    <span style="left:118px;color:var(--blue)">Block Storage</span>
    <span style="left:180px;color:var(--white)">Load Balancers</span>
    <span style="left:246px;color:var(--white)">Floating IPS</span>
  </div>
  <div class="abs" style="left:118px;top:972px;width:34px;height:1px;background:var(--blue)"></div>
  <div class="abs" style="left:64px;top:1004px;font-size:3.6px;color:var(--white)">Block Storage</div>
  <p class="small abs" style="left:64px;top:1014px;width:132px;color:var(--muted-light)">Block storage is an approach to data storage in which each storage volume acts as an individual hard drive the configured by the storage administrator. In the block storage model is data is saved to the storage media in fixed-sized blocks.</p>
  <div class="btn" style="left:64px;top:1054px;width:40px;height:13px">Explore Now</div>
  <div class="placeholder" role="img" aria-label="Floating isometric cubes in graphite, lime, orange and stone" style="left:240px;top:990px;width:85px;height:90px;background:linear-gradient(135deg,var(--graphite) 0%,var(--lime) 45%,var(--orange) 70%,var(--stone) 100%);opacity:.8"></div>

  <section class="section-light" style="top:1106px;height:303px">
    <h2 class="heading abs center" style="top:30px">Choose your perfect web<br>hosting plan</h2>
    <p class="small abs center" style="top:66px">Each web hosting plan comes with a free domain name</p>
    <div class="btn" style="left:166px;top:79px;width:32px;height:11px;font-size:3px">Monthly</div>
    <div class="btn" style="left:198px;top:79px;width:29px;height:11px;font-size:3px;background:var(--white);color:var(--text-dark)">Yearly</div>
  </section>
  <div class="plan" style="left:75px;width:73px">
    <h4>STARTUP</h4><p class="tag">Best for small business owners</p>
    <p class="price"><sup>$</sup>99<sub>/mo</sub></p>
    <ul><li>2x CPU Power</li><li>Free Migration</li><li>Limited Reporting</li><li>500GB ALL SSD Storage</li></ul>
    <div class="cta">Start 14 Days Trial</div><p class="note">No credit card required</p>
  </div>
  <div class="plan" style="left:155px;width:81px;top:1215px;height:167px;padding-top:17px;box-shadow:0 2px 6px rgba(0,0,0,.08)">
    <div class="abs" style="left:0;top:0;width:81px;height:6px;background:var(--text-dark);color:var(--white);font-size:2.6px;line-height:6px">MOST POPULAR</div>
    <h4>AGENCY</h4><p class="tag">Best for medium agency</p>
    <p class="price"><sup>$</sup>199<sub>/mo</sub></p>
    <ul><li>16x CPU Power</li><li>Free Migration</li><li>Unlimited Websites</li><li>1000GB ALL SSD Storage</li><li>Shared environment</li><li>Unlimited Bandwidth</li></ul>
    <div class="cta primary">Start 14 Days Trial</div><p class="note">No credit card required</p>
  </div>
  <div class="plan" style="left:242px;width:75px">
    <h4>DEVELOPER</h4><p class="tag">Best for independent developers</p>
    <p class="price"><sup>$</sup>69<sub>/mo</sub></p>
    <ul><li>4x CPU Power</li><li>300GB ALL SSD Storage</li><li>16x CPU Power</li><li class="off">Dedicated environment</li></ul>
    <div class="cta">Start 14 Days Trial</div><p class="note">No credit card required</p>
  </div>

  <h2 class="heading abs" style="left:38px;top:1446px;color:var(--white)">See what these customers<br>have to say</h2>
  <div class="placeholder" role="img" aria-label="Portrait photo of a customer in a dark sweater" style="left:38px;top:1487px;width:84px;height:88px;background:linear-gradient(180deg,#c9ced6 0%,#8e97a3 100%)"></div>
  <p class="quote" style="left:38px;top:1584px;width:88px">"I cannot believe that I have got a brand new landing page after getting Atlas. It was super easy to edit and faster and easier to work &amp; increases our exposure."</p>
  <p class="who" style="left:38px;top:1618px">Hanna Vogt</p><p class="role" style="left:38px;top:1624px">Chief Marketing Officer</p>

  <p class="quote" style="left:150px;top:1537px;width:84px">"Awesome experience working with the team at Northfield Studio Always very responsive and continuously gives us suggestions to improve our business."</p>
  <p class="who" style="left:150px;top:1571px">Tobias Reed</p><p class="role" style="left:150px;top:1577px">Co-Founder</p>
  <div class="placeholder" role="img" aria-label="Portrait photo of a smiling customer in a light blazer" style="left:150px;top:1590px;width:91px;height:95px;background:linear-gradient(180deg,#e9e9e7 0%,#b9b6b0 100%)"></div>

  <div class="placeholder" role="img" aria-label="Portrait photo of a customer in a dark blazer" style="left:266px;top:1497px;width:88px;height:93px;background:linear-gradient(180deg,#9fb3a8 0%,#4c5d55 100%)"></div>
  <p class="quote" style="left:266px;top:1598px;width:88px">"You made it so simple. My new site is so much faster and easier to work with than my old site. I just choose the page, make the change &amp; it is a good channel for us."</p>
  <p class="who" style="left:266px;top:1632px">Mira Castell</p><p class="role" style="left:266px;top:1638px">Founder</p>

  <div class="abs" style="left:38px;top:1735px;width:316px;height:39px;background:var(--blue);border-radius:2px">
    <p class="heading abs" style="left:11px;top:10px;font-size:7px;line-height:9px;color:var(--white)">Stop worrying about hosting<br>problems</p>
    <div class="btn" style="left:253px;top:14px;width:53px;height:12px;background:var(--ink-dark)">Sign Up Now</div>
  </div>

  <footer class="footer">
    <h5 style="left:38px">Company</h5><h5 style="left:117px">Help</h5><h5 style="left:207px">Resources</h5><h5 style="left:300px">Links</h5>
    <a style="left:38px;top:1812px">About</a><a style="left:38px;top:1822px">Features</a><a style="left:38px;top:1832px">Works</a><a style="left:38px;top:1842px">Career</a>
    <a style="left:117px;top:1812px">Customer Support</a><a style="left:117px;top:1822px">Delivery Details</a><a style="left:117px;top:1832px">Terms &amp; Conditions</a><a style="left:117px;top:1842px">Privacy Policy</a>
    <a style="left:207px;top:1812px">Free eBooks</a><a style="left:207px;top:1822px">Development Tutorial</a><a style="left:207px;top:1832px">How to - Blog</a><a style="left:207px;top:1842px">Video Playlist</a>
    <a style="left:300px;top:1812px">Free eBooks</a><a style="left:300px;top:1822px">Development Tutorial</a><a style="left:300px;top:1832px">How to - Blog</a><a style="left:300px;top:1842px">Video Playlist</a>
  </footer>
</main>
</div>
</body>
</html>
```